Easter. Company for collection, treatment and recovery of dangerous and dangerous goods. not dangerous

We need an image folder with 4 pages, details see insert, logo can not be changed and some pictures collection and treatment of hazardous and non-hazardous waste, Tankwageninnenreinigung own fleet

Target Market(s)

existing customers and new customers

Colors

Designer to choose colors to be used in the design.

Requirements
Must have
• KARVO logo
Nice to have
• Design the text and the pictures so that it suits our disposal company. You can also use the pictures from our webside.

```html
<!DOCTYPE html>
<html lang="de">
<head>
<meta charset="utf-8">
<title>KARVO Mappe – Außenseite</title>
<link href="https://fonts.googleapis.com/css2?family=Montserrat:wght@400;500;600;700;800&display=swap" rel="stylesheet">
<style>
  :root {
    --bg: #eeeeee;
    --paper: #ffffff;
    --green: #2fb52a;
    --green-bright: #3cd12f;
    --green-dark: #0f4a1c;
    --green-deep: #0a3514;
    --text: #333333;
    --grey: #9a9a9a;
  }
  * { margin: 0; padding: 0; box-sizing: border-box; }
  html, body { width: 1200px; height: 809px; overflow: hidden; background: var(--bg); }
  body { font-family: "Montserrat", sans-serif; color: var(--text); position: relative; }

  .page { position: absolute; top: 24px; width: 540px; height: 761px; background: var(--paper); overflow: hidden; box-shadow: 0 4px 18px rgba(0,0,0,.18); }
  .page--back { left: 60px; }
  .page--front { left: 600px; }

  .corner-accent { position: absolute; left: 0; top: 0; }

  .photo { position: absolute; }
  .photo--tanker { left: 270px; top: 30px; width: 250px; height: 160px; background: linear-gradient(135deg, #d8d8d8, #7a7a7a 55%, #3c3c3c); clip-path: polygon(8% 18%, 100% 0, 100% 88%, 0 100%); }
  .photo--site { left: 0; top: 165px; width: 540px; height: 270px; background: linear-gradient(160deg, #b9c7d8 0%, #8fa0b4 30%, #5d6b74 55%, #3f5a3a 80%, #2f4a2a 100%); clip-path: polygon(0 28%, 100% 0, 100% 82%, 0 100%); }
  .accent-bar { position: absolute; left: 200px; top: 188px; width: 200px; height: 8px; background: var(--green-bright); transform: rotate(-9deg); transform-origin: left; }

  .intro { position: absolute; left: 30px; top: 455px; width: 480px; font-size: 10.5px; line-height: 1.55; text-align: justify; }
  .since { position: absolute; left: 30px; top: 540px; font-size: 12.5px; font-weight: 600; color: var(--green); }

  .badges { position: absolute; left: 40px; top: 575px; display: flex; gap: 62px; align-items: center; }
  .badge { width: 50px; height: 50px; border-radius: 50%; background: #f0a33a; border: 4px solid #d9d9d9; }
  .badge--rect { width: 70px; height: 28px; border-radius: 3px; background: #8fb0c9; border: none; }
  .badge--blue { width: 56px; height: 34px; border-radius: 50%; background: #3b6fb5; border: none; }

  .brand { font-weight: 800; color: var(--green-dark); letter-spacing: 3px; }
  .brand--back { position: absolute; left: 205px; top: 638px; font-size: 26px; }

  .contacts { position: absolute; left: 30px; top: 680px; display: flex; gap: 22px; font-size: 11.5px; font-weight: 600; }
  .contacts span { display: flex; align-items: center; gap: 6px; }
  .dot-icon { width: 11px; height: 11px; border-radius: 50%; background: var(--green); }

  .emergency-band { position: absolute; left: 0; bottom: 0; width: 540px; height: 70px; background: var(--green-dark); clip-path: polygon(0 22%, 14% 22%, 22% 0, 100% 0, 100% 100%, 0 100%); }
  .emergency { position: absolute; left: 30px; bottom: 14px; font-size: 24px; font-weight: 800; color: var(--green-bright); }
  .emergency b { color: #fff; font-weight: 800; }

  .brand--front { position: absolute; left: 0; width: 540px; top: 42px; text-align: center; font-size: 42px; }
  .front-bar { position: absolute; right: 0; top: 115px; width: 200px; height: 8px; background: var(--green-bright); }
  .photo--terraces { left: 0; top: 123px; width: 540px; height: 420px; background: linear-gradient(170deg, #c9d3dc 0%, #7f8c6a 22%, #6aa13b 45%, #4c8a2a 65%, #6b4a2c 100%); clip-path: polygon(0 0, 100% 0, 100% 72%, 0 100%); }
  .services-area { position: absolute; left: 0; top: 420px; width: 540px; height: 341px; background: linear-gradient(180deg, var(--green-dark), var(--green-deep)); clip-path: polygon(0 35%, 35% 20%, 100% 0, 100% 100%, 0 100%); }

  .services { position: absolute; left: 20px; top: 540px; list-style: none; display: flex; flex-direction: column; align-items: center; width: 500px; gap: 8px; }
  .services li { display: flex; align-items: center; gap: 10px; color: #fff; font-size: 15px; font-weight: 500; }
  .services .label { border: 1px dashed var(--green); border-radius: 10px; padding: 3px 14px; }
  .arrow-icon { width: 16px; height: 16px; }

  .web-strip { position: absolute; right: 0; bottom: 22px; width: 230px; height: 16px; background: var(--green); clip-path: polygon(6% 0, 100% 0, 100% 100%, 0 100%); }
  .web { position: absolute; right: 20px; bottom: 24px; font-size: 10px; letter-spacing: 6px; color: #fff; }
</style>
</head>
<body>
  <section class="page page--back">
    <svg class="corner-accent" width="80" height="110" viewBox="0 0 80 110">
      <polygon points="0,10 50,0 0,60" fill="var(--green-bright)"/>
      <polygon points="0,60 60,45 0,105" fill="#8a8a8a"/>
    </svg>
    <div class="photo photo--tanker" role="img" aria-label="Schwarzweißfoto eines Tankwagens an der Befüllstation"></div>
    <div class="photo photo--site" role="img" aria-label="Luftbild des Firmengeländes mit Hallen und Fahrzeugen"></div>
    <div class="accent-bar"></div>

    <p class="intro">Firma KARVO Umweltschutz und Wertstoff-Recycling GmbH &amp; Co KG ist ein modernes, mittelständisches privates Dienstleistungsunternehmen im Zentralraum Nordtal, welches mit jeweils dem Stand der Technik entsprechender Verfahrenstechnik eine Vielzahl unterschiedlichster Problemlösungen im Bereich der Entsorgungs- und Recyclingwirtschaft als auch Tankwagenreinigungen anbietet.</p>
    <p class="since">KARVO ist seit 1976 am Standort, Gewerbering 12, in Steinfeld tätig.</p>

    <div class="badges">
      <div class="badge badge--rect"></div>
      <div class="badge"></div>
      <div class="badge"></div>
      <div class="badge badge--blue"></div>
    </div>

    <div class="brand brand--back">KARVO</div>

    <div class="contacts">
      <span><i class="dot-icon"></i>0043/7000/11200</span>
      <span><i class="dot-icon"></i>0043/7000/11299</span>
      <span><i class="dot-icon"></i>www.karvo.at</span>
    </div>

    <div class="emergency-band"></div>
    <p class="emergency">24h Notdienst: <b>0699/00 12 34 56</b></p>
  </section>

  <section class="page page--front">
    <div class="brand brand--front">KARVO</div>
    <div class="front-bar"></div>
    <div class="photo photo--terraces" role="img" aria-label="Grüne Reisterrassen in Berglandschaft mit Gegenlicht"></div>
    <div class="services-area"></div>

    <ul class="services">
      <li><svg class="arrow-icon" viewBox="0 0 16 16"><circle cx="8" cy="8" r="8" fill="var(--green)"/><path d="M6 4l4 4-4 4" stroke="#fff" stroke-width="2" fill="none"/></svg><span class="label">Abfallsammlung</span></li>
      <li><svg class="arrow-icon" viewBox="0 0 16 16"><circle cx="8" cy="8" r="8" fill="var(--green)"/><path d="M6 4l4 4-4 4" stroke="#fff" stroke-width="2" fill="none"/></svg><span class="label">Abfallbehandlung</span></li>
      <li><svg class="arrow-icon" viewBox="0 0 16 16"><circle cx="8" cy="8" r="8" fill="var(--green)"/><path d="M6 4l4 4-4 4" stroke="#fff" stroke-width="2" fill="none"/></svg><span class="label">Abfallentsorgung</span></li>
      <li><svg class="arrow-icon" viewBox="0 0 16 16"><circle cx="8" cy="8" r="8" fill="var(--green)"/><path d="M6 4l4 4-4 4" stroke="#fff" stroke-width="2" fill="none"/></svg><span class="label">Reinigung von Industrieanlagen und Behälter</span></li>
      <li><svg class="arrow-icon" viewBox="0 0 16 16"><circle cx="8" cy="8" r="8" fill="var(--green)"/><path d="M6 4l4 4-4 4" stroke="#fff" stroke-width="2" fill="none"/></svg><span class="label">Tankwageninnenreinigung</span></li>
    </ul>

    <div class="web-strip"></div>
    <span class="web">www.karvo.at</span>
  </section>
</body>
</html>
```